Jewellery Company Needs an Authenticity Card Design

We need an authenticity card designed for a pearl jewellery company. It will be a folded card in portrait mode. The size of the card is 110mm by 85mm (flat unfolded). After folding, the size of the card is 55mm in width and 85mm in length. The bleed for the artwork is 3mm.
We’re looking for a very elegant and luxurious style for the card. We want the card to have a neutral white background with a simple, classy and delicate pattern background so it’s not completely white. At the same time, we don’t want the background pattern to be overwhelming or cheesy. We want the text colour to be in dark grey and the text to stand out from the card.
The text for the front cover:
Doran Vale(logo font type “Allerta Stencil”), Contemporary Fine Pearl Jewellery and the website url address www.qemt-vorin.com
Inside Left:
Congratulations on this awesome new addition to your jewellery collection!
Inside Right:
We certify that the pearl(s) used to create this piece of jewellery is/(are) 100% authentic cultured pearl(s) directly from the environmentally responsible pearl farms. Each pearl has been individually selected by our skilled experts for its unique beauty and fine quality.
We are proud that we only work with ethical pearl farms and partners that share our reverence for environmental and social sustainability.
The text for the back cover:
hab pl dic quisq sa puru sita a vole. cont m nucjk co nisi vitae sust us.
Company logo and the website url Doran Vale www.qemt-vorin.com
Please use your creativity for this design and make sure the feel for the card is luxurious and elegant. We do not want anything looking cheap or cheesy.
Additional Information:
The paper we'll be using for this card is ice gold. It looks very premium and luxurious and has a shiny surface to it almost like the mother of pearl which is perfect for the purpose of this card. So the design needs to be classy, modern and sophisticated.
For font type ideas and the overall look and feel, please check out these two websites for the look and feel. ( Morvento Gems https://www.morvento.com and Tovanijewellery https://www.tovanijewellery.com.au/)
Please see attached the example cover pattern from Tovanijewellery catalog. It's quite subtle and looks polished. Please note that we want the card background to be white but with the subtle pattern or texture and not coloured like the one in the attached example.
Updates
Hi, I've updated the original brief to include the following information that you might find helpful.
Additional Information:

```html
<!DOCTYPE html>
<html lang="en">
<head>
<meta charset="utf-8">
<title>Doran Vale — Authenticity Card</title>
<link rel="stylesheet" href="https://fonts.googleapis.com/css2?family=Allerta+Stencil&family=Allerta&display=swap">
<style>
  :root {
    --stage: #d5d9da;
    --panel-light: #fbfbfb;
    --panel-mid: #e9e9e9;
    --panel-deep: #dcdcdc;
    --card-face: #f3f3f3;
    --rule: #4a4a4a;
    --ink: #4b4b4b;
    --ink-soft: #5a5a5a;
    --ornament: #c9c9c9;
  }
  html, body {
    margin: 0;
    padding: 0;
    width: 1200px;
    height: 534px;
    overflow: hidden;
    background: var(--stage);
  }
  .spread {
    position: relative;
    width: 1200px;
    height: 534px;
  }
  .panel {
    position: absolute;
    top: 60px;
    width: 284px;
    height: 422px;
    box-shadow: 2px 3px 6px rgba(0,0,0,0.18);
    overflow: hidden;
  }
  .panel-pattern {
    position: absolute;
    inset: 0;
    background:
      radial-gradient(ellipse at 30% 40%, var(--panel-light) 0%, transparent 60%),
      linear-gradient(160deg, var(--panel-light) 0%, var(--panel-mid) 55%, var(--panel-deep) 100%);
  }
  .panel--front { left: 14px; }
  .panel--inside-left { left: 311px; }
  .panel--inside-right { left: 604px; }
  .panel--back { left: 898px; }

  .brand-name {
    font-family: "Allerta Stencil", sans-serif;
    color: var(--ink);
    margin: 0;
    font-weight: 400;
    position: absolute;
    left: 0;
    right: 0;
    text-align: center;
  }
  .body-text {
    font-family: "Allerta", sans-serif;
    color: var(--ink);
    margin: 0;
    position: absolute;
    left: 0;
    right: 0;
    text-align: center;
  }
  .web-address {
    font-family: "Allerta Stencil", sans-serif;
    color: var(--ink-soft);
    position: absolute;
    left: 0;
    right: 0;
    text-align: center;
    letter-spacing: 0.5px;
  }

  /* Front cover */
  .panel--front .brand-name { top: 206px; font-size: 45px; letter-spacing: 1px; }
  .panel--front .tagline { top: 262px; font-size: 13.5px; letter-spacing: 0.3px; color: var(--ink-soft); }
  .panel--front .web-address { top: 381px; font-size: 14px; }

  /* Inset cards */
  .inset-card {
    position: absolute;
    top: 42px;
    left: 19px;
    width: 246px;
    height: 336px;
    background: var(--card-face);
    box-shadow: 0 2px 6px rgba(0,0,0,0.18);
  }
  .inset-frame {
    position: absolute;
    top: 12px;
    left: 10px;
    width: 222px;
    height: 312px;
    border: 1px solid var(--rule);
    box-sizing: border-box;
  }
  .ornament {
    position: absolute;
    display: block;
  }
  .panel--inside-left .ornament { top: 62px; left: 40px; }
  .panel--inside-right .ornament { top: 24px; left: 41px; }

  .greeting {
    font-family: "Allerta Stencil", sans-serif;
    color: var(--ink);
    position: absolute;
    top: 108px;
    left: 0;
    right: 0;
    margin: 0;
    text-align: center;
    font-size: 21px;
    line-height: 25px;
    letter-spacing: 0.3px;
  }

  .certificate {
    position: absolute;
    top: 94px;
    left: 4px;
    right: 4px;
    font-family: "Allerta", sans-serif;
    color: var(--ink);
    font-size: 11.3px;
    line-height: 13.8px;
    text-align: center;
  }
  .certificate p { margin: 0 0 13.8px; }

  /* Back cover */
  .panel--back .closing-note { top: 231px; font-size: 11.5px; line-height: 14.5px; color: var(--ink-soft); }
  .panel--back .brand-name { top: 388px; font-size: 32px; letter-spacing: 0.8px; }
  .panel--back .web-address { top: 381px; font-size: 14.5px; color: var(--ink); }
  .panel--back .brand-name { top: 344px; }
</style>
</head>
<body>
<main class="spread">

  <section class="panel panel--front">
    <div class="panel-pattern" role="img" aria-label="Subtle white quilted diamond pattern"></div>
    <h1 class="brand-name">Doran Vale</h1>
    <p class="body-text tagline">Contemporary Fine Pearl Jewellery</p>
    <span class="web-address">www.qemt-vorin.com</span>
  </section>

  <section class="panel panel--inside-left">
    <div class="panel-pattern" role="img" aria-label="Subtle white quilted diamond pattern"></div>
    <div class="inset-card">
      <div class="inset-frame"></div>
      <svg class="ornament" width="158" height="46" viewBox="0 0 158 46" role="img" aria-label="Silver filigree flourish ornament">
        <defs>
          <linearGradient id="ornFadeL" x1="0" x2="1">
            <stop offset="0" stop-color="#d6d6d6"/>
            <stop offset="0.5" stop-color="#bdbdbd"/>
            <stop offset="1" stop-color="#e6e6e6"/>
          </linearGradient>
        </defs>
        <rect x="0" y="10" width="158" height="26" rx="13" fill="url(#ornFadeL)" opacity="0.55"/>
      </svg>
      <p class="greeting">Congratulations<br>on this awesome<br>new addition<br>to your jewellery<br>collection!</p>
    </div>
  </section>

  <section class="panel panel--inside-right">
    <div class="panel-pattern" role="img" aria-label="Subtle white quilted diamond pattern"></div>
    <div class="inset-card">
      <div class="inset-frame"></div>
      <svg class="ornament" width="160" height="48" viewBox="0 0 160 48" role="img" aria-label="Silver filigree flourish ornament">
        <defs>
          <linearGradient id="ornFadeR" x1="0" x2="1">
            <stop offset="0" stop-color="#d6d6d6"/>
            <stop offset="0.5" stop-color="#bdbdbd"/>
            <stop offset="1" stop-color="#e6e6e6"/>
          </linearGradient>
        </defs>
        <rect x="0" y="10" width="160" height="28" rx="14" fill="url(#ornFadeR)" opacity="0.55"/>
      </svg>
      <div class="certificate">
        <p>We certify that the pearl(s) used<br>to create this piece of jewellery<br>is/(are) 100% authentic cultured<br>pearl(s) directly from the<br>environmentally responsible pearl<br>farms. Each pearl has been<br>individually selected by our skilled<br>experts for its unique beauty<br>and fine quality.</p>
        <p>We are proud that we only work<br>with ethical pearl farms and<br>partners that share our reverence<br>for environmental and social<br>sustainability.</p>
      </div>
    </div>
  </section>

  <section class="panel panel--back">
    <div class="panel-pattern" role="img" aria-label="Subtle white quilted diamond pattern"></div>
    <p class="body-text closing-note">hab pl dic quisq sa puru sita a vole.<br>cont m nucjk co nisi vitae sust us.</p>
    <h2 class="brand-name">Doran Vale</h2>
    <span class="web-address">www.qemt-vorin.com</span>
  </section>

</main>
</body>
</html>
```